Flyer Design for a Boston Therapeutic Clinic

I am a body therapist who needs a couple of flyers designed:
1. To fit half a page.
2. To fit a 5 inch by 3.5 inch flyer.
My practice is based in Boston, MA and my web site is:
www.LarchTessvik.Com
For the First half page:
A. Have my company's name and color shown as it appears on my web site (Larch Tessvik)
B. Have the following text: "Control your weight (This part should be emphasized) by balancing your nervous and digestive system through the Tessvik Method. The Tessvik Method, a technique developed by Dr. Mara. Tessvik, uses physical pressure to manipulate visceral tissue to bring back resiliency and proper functioning of the whole body."
Also helps with
-Constipation
-Bloating
-IBS
-eating disorders and overeating
Our practitioner is highly experienced. Please visit our web sites for reviews.
C. I would like to have a nice earthy feeling, something that feels "freeing" like open flowers, or an open land scape such as mountains or fields.
D. I also like the color blue, white, orange; perhaps if these colors can be integrated into the flyer, that would be great.
E. "Visit our web site LarchTessvik.com or call 786-555-0148"
The Smaller Flyer :
A.The smaller Flyer should also have my Company's name as shown on my web site (Larch Tessvik)
B.The following text: " Restore your body's natural resiliency and greatly reduce your physical pain through the Dr. Mara Tessvik Method of Structural Integration."
C. "Our practitioner is highly experienced and has a great reputation; visit our web site for reviews."
"Benefits:
"reduce aches and pains
reduce joint pain
reduce chronic muscular tension"
D, "feel better after the first session!"
E. if you could use a picture of me working on someone from my web site, that would be great.
F. I also like the colors white, orange and silver, for this one.
G. "Visit our web site LarchTessvik.com or call 786-555 0148"
I am very open minded,
I would like the flyer to evoke a sense of tranquility, professionalism, and simplicity. So if you have another angle you think would look good, then go for it! As long as it looks clean, professional and helpful.
Thanks a lot!
If you need any pictures from my web site, I have the original high resolution files that i can send.
Professionals and working men and women from ages 20-70
Clinic

```html
<!DOCTYPE html>
<html lang="en">
<head>
<meta charset="UTF-8">
<title>Larch Tessvik – Structural Integration Flyer</title>
<link rel="stylesheet" href="https://fonts.googleapis.com/css2?family=Alfa+Slab+One&family=Arvo:wght@700&family=Bree+Serif&family=Oswald:wght@700&display=swap">
<style>
  :root {
    --green: #62bb46;
    --blue: #00aeef;
    --teal: #45c1a8;
    --black: #000000;
    --orange: #ef5a28;
    --red: #ee3b2f;
    --teal-text: #1a9a86;
    --ink: #1a1a1a;
    --panel-light: #e6e7ea;
    --panel-mid: #c9cbcf;
    --panel-dark: #8d8f93;
    --white: #ffffff;
  }
  * { margin: 0; padding: 0; box-sizing: border-box; }
  html, body { width: 840px; height: 1200px; overflow: hidden; background: var(--white); }
  .flyer { position: relative; width: 840px; height: 1200px; }

  .frame { position: absolute; left: 10px; top: 6px; width: 820px; height: 1184px; border: 3px solid var(--black); overflow: hidden; }
  .band { position: absolute; left: 0; width: 100%; }
  .band--green-top { top: 0; height: 166px; background: var(--green); }
  .band--blue-top { top: 166px; height: 328px; background: var(--blue); }
  .band--teal { top: 494px; height: 280px; background: var(--teal); }
  .band--blue-low { top: 774px; height: 216px; background: var(--blue); }
  .band--green-low { top: 990px; height: 200px; background: var(--green); }

  .panel {
    position: absolute; left: 24px; top: 268px; width: 776px; height: 902px;
    background: radial-gradient(ellipse 75% 70% at 42% 45%, var(--panel-light) 55%, var(--panel-mid) 85%, var(--panel-dark) 100%);
  }
  .crest { position: absolute; left: 0; top: 0; width: 840px; height: 380px; }

  .line { position: absolute; left: 0; width: 840px; text-align: center; white-space: nowrap; }

  .brand { top: 70px; font-family: "Arvo", serif; font-weight: 700; font-size: 66px; color: var(--orange); letter-spacing: 1px; }
  .web-top { top: 152px; font-family: "Alfa Slab One", serif; font-size: 28px; color: var(--red);
    text-shadow: -1px -1px 0 var(--white), 1px -1px 0 var(--white), -1px 1px 0 var(--white), 1px 1px 0 var(--white); }
  .tel { top: 196px; font-family: "Alfa Slab One", serif; font-size: 38px; color: var(--teal-text);
    text-shadow: -1px -1px 0 #7a6a3a, 1px -1px 0 #7a6a3a, -1px 1px 0 #7a6a3a, 1px 1px 0 #7a6a3a; }
  .visit-practitioner { top: 262px; font-family: "Alfa Slab One", serif; font-size: 44px; color: var(--white);
    text-shadow: -2px -2px 0 #333, 2px -2px 0 #333, -2px 2px 0 #333, 2px 2px 0 #333, 3px 3px 0 #666; }
  .visit-practitioner .name { color: var(--red); }
  .address { font-family: "Arvo", serif; font-weight: 700; font-size: 27px; line-height: 36px; color: var(--ink); }
  .address--street { top: 320px; }
  .address--city { top: 356px; }

  .gallery { position: absolute; left: 68px; top: 392px; width: 714px; height: 192px; background: var(--black); }
  .photo { position: absolute; top: 14px; height: 160px; width: 220px; }
  .photo--session { left: 14px; background: linear-gradient(135deg, #b8652a, #e2a060 45%, #7a3a18); }
  .photo--practitioner { left: 246px; background: linear-gradient(135deg, #e07a2a, #c8501c 50%, #5a3a48); }
  .photo--storefront { left: 481px; width: 217px; background: linear-gradient(160deg, #8fae6a, #4f7a3a 45%, #3a5f9a 70%, #d8d4cc); }

  .copy { position: absolute; left: 0; width: 840px; text-align: center; font-family: "Bree Serif", serif; font-size: 22px; line-height: 32px; color: var(--ink); }
  .copy--intro { top: 600px; }
  .copy--reputation { top: 720px; }

  .benefits-title { top: 818px; font-family: "Alfa Slab One", serif; font-size: 44px; line-height: 56px; color: var(--green);
    text-shadow: -2px -2px 0 #1b1b1b, 2px -2px 0 #1b1b1b, -2px 2px 0 #1b1b1b, 2px 2px 0 #1b1b1b; }
  .benefits { position: absolute; top: 876px; left: 0; width: 840px; list-style: none; text-align: center;
    font-family: "Bree Serif", serif; font-size: 23px; line-height: 33px; color: var(--ink); }

  .promise { top: 980px; font-family: "Oswald", sans-serif; font-weight: 700; font-size: 54px; line-height: 72px; color: var(--green); letter-spacing: -1px;
    text-shadow: -2px -2px 0 #1b1b1b, 2px -2px 0 #1b1b1b, -2px 2px 0 #1b1b1b, 2px 2px 0 #1b1b1b; }
  .cta { font-family: "Alfa Slab One", serif; font-size: 33px; line-height: 44px; color: var(--red);
    text-shadow: -2px -2px 0 var(--white), 2px -2px 0 var(--white), -2px 2px 0 var(--white), 2px 2px 0 var(--white); }
  .cta--web { top: 1054px; }
  .cta--call { top: 1102px; }
</style>
</head>
<body>
<div class="flyer">
  <div class="frame">
    <div class="band band--green-top"></div>
    <div class="band band--blue-top"></div>
    <div class="band band--teal"></div>
    <div class="band band--blue-low"></div>
    <div class="band band--green-low"></div>
    <div class="panel"></div>
  </div>

  <svg class="crest" viewBox="0 0 840 380" aria-hidden="true">
    <path d="M16 172 Q422 -156 828 172 L640 368 L590 316 L250 316 L208 368 Z" fill="#000"/>
  </svg>

  <div class="line brand">Larch Tessvik</div>
  <div class="line web-top">WWW.LARCHTESSVIK.COM</div>
  <div class="line tel">Tel: (786) 555-0148</div>
  <div class="line visit-practitioner">Visit <span class="name">Owen Marchetti</span> At:</div>
  <div class="line address address--street">418 Alder St.</div>
  <div class="line address address--city">Boston, MA 02116</div>

  <div class="gallery">
    <div class="photo photo--session" role="img" aria-label="Photo of the practitioner's hands working on a client's neck"></div>
    <div class="photo photo--practitioner" role="img" aria-label="Photo of the practitioner treating a client's knee"></div>
    <div class="photo photo--storefront" role="img" aria-label="Photo of the clinic's street front with trees and awnings"></div>
  </div>

  <p class="copy copy--intro">Restore your body’s natural resiliency and greatly<br>reduce your physical pain through the Dr. Mara Tessvik<br>Method of Structural Integration.</p>
  <p class="copy copy--reputation">Our certified practitioner, is highly experienced<br>andhas a great reputation; visit our website<br>for reviews</p>

  <div class="line benefits-title">Benefits</div>
  <ul class="benefits">
    <li>-reduce aches and pains</li>
    <li>-reduce joint pain</li>
    <li>-reduce chronic muscular tension</li>
  </ul>

  <div class="line promise">Feel better after the first session!</div>
  <div class="line cta cta--web">Visit our web site LarchTessvik.com</div>
  <div class="line cta cta--call">or call 786-555 0148</div>
</div>
</body>
</html>
```